We Need a Letterhead + Fax Cover Sheet for Heron Staffing

LETTERHEAD:
- Simple letterhead. Please provide an editable .doc file apart from usual Source Files. Logo Files attached for your use.
- Please place our logo on the upper right corner of the page. You may add some sort of graphic, or light colored background (depends on what looks good).
- Footer should include:
Heron Staffing, LLC
412 Kestrel Ave. Suite 118
Mobile, AL 36619

FAX COVER SHEET:
- Have the logo placed here, should be large, maybe an eight of the page.
- Put:
From:
To:
Phone Number:
Fax Number:

*Still needs some details, will update you because working on the website, etc.

Heron Coastal Workforce Services

```html
<!DOCTYPE html>
<html lang="en">
<head>
<meta charset="utf-8">
<title>Heron Staffing – Letterhead and Fax Cover Sheet</title>
<link rel="stylesheet" href="https://fonts.googleapis.com/css2?family=Lato:wght@400;700&family=Roboto:wght@300;400;700&display=swap">
<style>
  :root {
    --backdrop: #d4d4d4;
    --paper: #ffffff;
    --green: #8aa83a;
    --blue: #0b6fb4;
    --ink: #333333;
    --fax-grey: #9a9a9a;
    --rule-grey: #b5b5b5;
  }
  * { box-sizing: border-box; margin: 0; padding: 0; }
  html, body { width: 1200px; height: 1200px; overflow: hidden; background: var(--backdrop); }
  body { position: relative; font-family: "Lato", sans-serif; color: var(--ink); }

  .sheet {
    position: absolute;
    width: 362px; height: 512px;
    background: var(--paper);
    box-shadow: 0 3px 8px rgba(0,0,0,0.22);
    overflow: hidden;
  }
  .sheet--letter-green { left: 208px; top: 56px;  --accent: var(--green); --second: var(--blue); }
  .sheet--fax-green    { left: 630px; top: 56px;  --accent: var(--green); --second: var(--blue); }
  .sheet--letter-blue  { left: 208px; top: 621px; --accent: var(--blue);  --second: var(--green); }
  .sheet--fax-blue     { left: 630px; top: 621px; --accent: var(--blue);  --second: var(--green); }

  .corner-band { position: absolute; left: 0; top: 0; width: 292px; height: 28px; }
  .corner-band .band-main { fill: var(--accent); }
  .corner-band .band-edge { fill: var(--second); }

  .brand {
    position: absolute;
    display: flex; flex-direction: column; align-items: center; justify-content: center;
    text-align: center;
    font-family: "Roboto", sans-serif; font-weight: 700;
    color: var(--blue);
    text-transform: uppercase;
    line-height: 1.15;
  }
  .brand__dot { border-radius: 50%; background: var(--green); margin-bottom: 5px; }
  .brand--small { left: 262px; top: 18px; width: 76px; height: 74px; font-size: 8.5px; }
  .brand--small .brand__dot { width: 22px; height: 22px; }
  .brand--large { left: 220px; top: 26px; width: 116px; height: 114px; font-size: 13px; }
  .brand--large .brand__dot { width: 34px; height: 34px; margin-bottom: 7px; }

  .fax-title {
    position: absolute; left: 33px; top: 34px;
    font-family: "Roboto", sans-serif; font-weight: 300;
    font-size: 42px; color: var(--fax-grey); letter-spacing: 0.5px;
  }

  .fax-fields {
    position: absolute; left: 34px; top: 170px; width: 294px;
    border-collapse: collapse;
    font-family: "Roboto", sans-serif; font-size: 5.5px; font-weight: 700;
  }
  .fax-fields td { height: 10.8px; border: 0.8px solid var(--rule-grey); padding: 0 4px; }
  .fax-fields .label { width: 35px; }
  .fax-fields .value { width: 129px; }

  .fax-notes {
    position: absolute; left: 34px; top: 234px; width: 294px; height: 220px;
    border: 0.8px solid var(--accent);
  }
  .status-bar {
    display: flex; height: 11px; background: var(--accent);
    font-family: "Roboto", sans-serif; font-size: 5px; font-weight: 700; color: #fff;
  }
  .status-bar span {
    flex: 1; display: flex; align-items: center; justify-content: center; gap: 2px;
    border-left: 0.8px solid rgba(255,255,255,0.7);
    white-space: nowrap;
  }
  .status-bar span:first-child { border-left: none; justify-content: flex-start; padding-left: 6px; flex: 0.7; }
  .status-bar .box { width: 3.5px; height: 3.5px; border: 0.5px solid #fff; display: inline-block; }
  .notes-label {
    text-align: center; margin-top: 13px;
    font-family: "Roboto", sans-serif; font-size: 5.5px; color: var(--ink);
  }

  .footer {
    position: absolute; left: 32px; top: 478px; width: 298px;
    border-top: 1.2px solid var(--accent);
    padding-top: 5px;
    text-align: center; font-size: 5px; color: var(--ink);
    white-space: nowrap;
  }
</style>
</head>
<body>

<!-- Letterhead, green accent -->
<section class="sheet sheet--letter-green">
  <svg class="corner-band" viewBox="0 0 292 28" aria-hidden="true">
    <polygon class="band-main" points="0,0 250,0 0,26"/>
    <polygon class="band-edge" points="250,0 292,0 0,28 0,26"/>
  </svg>
  <div class="brand brand--small"><span class="brand__dot"></span>Heron Coastal Workforce Services</div>
  <p class="footer">Heron Staffing, LLC &nbsp;|&nbsp; 412 Kestrel Ave. Suite 118 &nbsp; Pelican Bay, FL 36619</p>
</section>

<!-- Fax cover sheet, green accent -->
<section class="sheet sheet--fax-green">
  <svg class="corner-band" viewBox="0 0 292 28" aria-hidden="true">
    <polygon class="band-main" points="0,0 250,0 0,26"/>
    <polygon class="band-edge" points="250,0 292,0 0,28 0,26"/>
  </svg>
  <h1 class="fax-title">FAX</h1>
  <div class="brand brand--large"><span class="brand__dot"></span>Heron Coastal Workforce Services</div>
  <table class="fax-fields">
    <tr><td class="label">To:</td><td class="value"></td><td class="label">From:</td><td class="value"></td></tr>
    <tr><td class="label">Fax:</td><td class="value"></td><td class="label">Pages:</td><td class="value"></td></tr>
    <tr><td class="label">Phone:</td><td class="value"></td><td class="label">Date:</td><td class="value"></td></tr>
    <tr><td class="label">Re:</td><td class="value"></td><td class="label">CC:</td><td class="value"></td></tr>
  </table>
  <div class="fax-notes">
    <div class="status-bar">
      <span><i class="box"></i> Urgent</span>
      <span><i class="box"></i> For Review</span>
      <span><i class="box"></i> Please Comment</span>
      <span><i class="box"></i> Please Reply</span>
      <span><i class="box"></i> Confidential</span>
    </div>
    <p class="notes-label">COMMENTS:</p>
  </div>
  <p class="footer">Heron Staffing, LLC &nbsp;|&nbsp; 412 Kestrel Ave. Suite 118 &nbsp; Pelican Bay, FL 36619</p>
</section>

<!-- Letterhead, blue accent -->
<section class="sheet sheet--letter-blue">
  <svg class="corner-band" viewBox="0 0 292 28" aria-hidden="true">
    <polygon class="band-main" points="0,0 250,0 0,26"/>
    <polygon class="band-edge" points="250,0 292,0 0,28 0,26"/>
  </svg>
  <div class="brand brand--small"><span class="brand__dot"></span>Heron Coastal Workforce Services</div>
  <p class="footer">Heron Staffing, LLC &nbsp;|&nbsp; 412 Kestrel Ave. Suite 118 &nbsp; Pelican Bay, FL 36619</p>
</section>

<!-- Fax cover sheet, blue accent -->
<section class="sheet sheet--fax-blue">
  <svg class="corner-band" viewBox="0 0 292 28" aria-hidden="true">
    <polygon class="band-main" points="0,0 250,0 0,26"/>
    <polygon class="band-edge" points="250,0 292,0 0,28 0,26"/>
  </svg>
  <h1 class="fax-title">FAX</h1>
  <div class="brand brand--large"><span class="brand__dot"></span>Heron Coastal Workforce Services</div>
  <table class="fax-fields">
    <tr><td class="label">To:</td><td class="value"></td><td class="label">From:</td><td class="value"></td></tr>
    <tr><td class="label">Fax:</td><td class="value"></td><td class="label">Pages:</td><td class="value"></td></tr>
    <tr><td class="label">Phone:</td><td class="value"></td><td class="label">Date:</td><td class="value"></td></tr>
    <tr><td class="label">Re:</td><td class="value"></td><td class="label">CC:</td><td class="value"></td></tr>
  </table>
  <div class="fax-notes">
    <div class="status-bar">
      <span><i class="box"></i> Urgent</span>
      <span><i class="box"></i> For Review</span>
      <span><i class="box"></i> Please Comment</span>
      <span><i class="box"></i> Please Reply</span>
      <span><i class="box"></i> Confidential</span>
    </div>
    <p class="notes-label">COMMENTS:</p>
  </div>
  <p class="footer">Heron Staffing, LLC &nbsp;|&nbsp; 412 Kestrel Ave. Suite 118 &nbsp; Pelican Bay, FL 36619</p>
</section>

</body>
</html>
```